International travel site frontpage redesign

We sell tours to Scandinavia through our website www.borealvoyagehub.com. The website has become a bit old fashioned and we are in the process of making the website responsive. As you can see from the attached pictures the website will be wider with the responsive design, and our current design does not fit anymore.

Here is what we are looking for:
- A website that reflects a trustworthy and quality oriented company.
- Making the website more modern looking, but still recognisable (we want to keep the colours).
- keeping in mind that the age group of our customers are from 20-80 years old (most in their 60s).
- We want to remove the popular tours part and are instead looking to replace this with picture boxes the following subjects Scandinavia Specialist, Special Offers, Contact, Norway (or Norway Tours), Sweden (or Sweden Tours), Iceland (or Iceland Tours), Combination Tours. Possibly also Lapland, Winter, Northern Lights, Fjords and Capitals. Some of these categories can be smaller or perhaps half boxes; i.e. Winter and Northern lights in one. If we end up with four boxes per line perhaps we could add a social media box next to the three first ones.
- The above means that the left hand meny with Norway Tours, Sweden Tours etc will be redundant.
- we will add another line to the search Box (on the top): Destinations
- The top menu will have the same categories, but we need to add languages as the website will be in English and German.
- The footer must be changed
- We can take away the box to the right where it says "your window to booking the best of our world"

Reason: One of the decission makers had to go away on business last minute.

Target Market(s)

Travelling to Scandinavia is not low cost, so the website needs to appeal to those that can afford to travel to our destination.
The age group of our customers are from 20-80 years old (most in their 60s).

Industry/Entity Type

Travel

Number of Pages Required

1 page

Requirements
Should not have
• Flashy or cheap looking special offers...

```html
<!DOCTYPE html>
<html lang="en">
<head>
<meta charset="utf-8">
<title>Boreal Voyage — Tours to Scandinavia</title>
<link href="https://fonts.googleapis.com/css2?family=Roboto:wght@300;400;500;700&display=swap" rel="stylesheet">
<style>
:root{
  --red:#8e0a0a;
  --red-dark:#6e0505;
  --title-red:#a30d0d;
  --ink:#333333;
  --muted:#666666;
  --white:#ffffff;
  --panel:rgba(20,20,20,.82);
  --select:#1c1c1c;
  --footer:#2d2b2b;
  --footer-line:#444040;
  --footer-text:#d8d8d8;
  --feed-blue:#3b5998;
  --link-blue:#3b5998;
}
*{box-sizing:border-box;margin:0;padding:0}
html,body{width:1200px;height:2244px;overflow:hidden}
body{position:relative;background:var(--white);font-family:'Roboto',Arial,sans-serif;color:var(--ink)}
.abs{position:absolute}

/* hero */
.hero{left:0;top:0;width:1200px;height:702px;
  background:linear-gradient(180deg,#2a67b8 0%,#6fa3d6 18%,#5f7f58 34%,#3f5d34 52%,#556a48 66%,#2fa3a0 80%,#0f6b70 100%)}
.masthead{left:102px;top:0;width:998px;height:92px;background:var(--white)}
.brand{left:14px;top:26px;display:flex;align-items:center;gap:12px;font-size:31px;font-weight:400;letter-spacing:1px;color:#3a3a3a;text-transform:uppercase}
.brand-mark{width:16px;height:16px;background:var(--red)}
.site-search{left:741px;top:24px;width:240px;height:41px;border:1px solid #cfcfcf;display:flex;align-items:center;padding-left:12px;gap:8px;font-size:12px;color:#888;letter-spacing:.5px}
.main-nav{left:102px;top:92px;width:998px;height:40px;background:var(--red);color:var(--white);font-size:13px;font-weight:500;text-transform:uppercase}
.main-nav span{position:absolute;top:12px}
.flag{display:inline-block;width:20px;height:13px;vertical-align:-2px;margin-right:7px}
.flag.en{background:linear-gradient(135deg,#1e3f8a 0 40%,#c8102e 40% 60%,#1e3f8a 60%)}
.flag.de{background:linear-gradient(180deg,#000 0 33%,#dd0000 33% 66%,#ffce00 66%)}

.caption{left:105px;top:388px;width:370px;height:84px;background:rgba(90,90,90,.45);padding:9px 0 0 0;color:var(--white)}
.caption h1{font-weight:300;font-size:33px;line-height:36px}
.caption p{font-weight:300;font-size:18px;line-height:24px}
.dots{left:103px;top:627px;display:flex;gap:8px}
.dots i{width:24px;height:24px;border:2px solid var(--white);border-radius:50%;position:relative}
.dots i.on::after{content:"";position:absolute;left:5px;top:5px;width:10px;height:10px;border-radius:50%;background:var(--white)}

.tour-finder{left:811px;top:247px;width:289px;height:330px;background:var(--panel);padding:20px 0 0 18px;color:var(--white)}
.tour-finder label{display:block;font-size:13px;font-weight:500;text-transform:uppercase;height:21px}
.tour-finder .select{width:249px;height:39px;background:var(--select);font-size:11px;text-transform:uppercase;display:flex;align-items:center;justify-content:space-between;padding:0 14px;margin-bottom:23px}
.tour-finder .find-btn{width:240px;height:48px;background:var(--red);font-size:19px;text-transform:uppercase;display:flex;align-items:center;justify-content:center;margin-top:-4px}

/* tiles */
.tile{width:245px;text-align:center}
.tile .photo{height:211px}
.tile h2{margin-top:15px;font-size:16px;font-weight:700;color:var(--title-red);text-transform:uppercase;line-height:20px}
.tile p{font-size:14px;line-height:18px;color:var(--ink)}
.tile a{display:block;margin-top:4px;font-size:14px;color:var(--title-red);text-decoration:none}

/* social feed */
.feed{left:853px;top:1356px;width:247px;height:305px;border:1px solid #b8bdc8;background:var(--white)}
.feed-head{height:22px;background:var(--feed-blue);color:var(--white);font-size:14px;font-weight:700;padding:2px 6px}
.feed-post{position:relative;height:85px;margin:0 16px 0 8px;border-bottom:1px solid #d7d7d7}
.feed-post .avatar{position:absolute;left:1px;top:14px;width:27px;height:27px;background:#5a5550}
.feed-post p{position:absolute;left:37px;top:9px;width:165px;font-size:12px;line-height:16.5px;color:#333}
.feed-post p b{font-weight:400;color:var(--link-blue)}
.feed-post .meta{position:absolute;left:37px;top:63px;font-size:11.5px;color:#999}
.feed-post .meta em{font-style:normal;color:var(--link-blue);margin-left:8px}
.feed-scroll{position:absolute;right:1px;top:23px;width:12px;height:280px;border-left:1px solid #ddd}
.feed-scroll i{position:absolute;left:2px;top:52px;width:8px;height:24px;border-radius:3px;background:#4a7bd0}
.feed-foot{position:absolute;left:8px;bottom:6px;font-size:11px;color:#333;display:flex;align-items:center;gap:6px}
.feed-foot i{width:12px;height:12px;background:var(--feed-blue)}

/* footer */
.site-footer{left:0;top:1682px;width:1200px;height:562px;background:var(--footer);color:var(--footer-text)}
.footer-col{position:absolute;top:32px}
.footer-col h3{font-size:15px;font-weight:500;color:var(--white);margin-bottom:7px}
.footer-col li{list-style:none;font-size:12px;line-height:28.6px}
.footer-col h3.second{margin-top:22px}
.footer-rule{position:absolute;top:30px;width:1px;height:360px;background:var(--footer-line)}
.footer-base{position:absolute;left:102px;top:442px;width:998px;height:1px;background:var(--footer-line)}
.connect{position:absolute;left:104px;top:470px;font-size:12px}
.social{position:absolute;left:103px;top:496px;display:flex;gap:8px}
.social i{width:45px;height:45px;border-radius:50%;background:#4a4747}
.payments{position:absolute;left:881px;top:473px;width:219px;height:40px;background:var(--white);display:flex;gap:6px;align-items:center;padding:0 6px}
.payments i{height:28px;flex:1;background:#d4d4d4}
.payments i:nth-child(1){background:#1a1f71}
.payments i:nth-child(3){background:#e2a33a}
.copyright{position:absolute;left:881px;top:517px;font-size:12px;color:var(--white)}
</style>
</head>
<body>

<section class="hero abs" role="img" aria-label="Limestone cliffs rising from a turquoise bay with a white outrigger boat"></section>

<header class="masthead abs">
  <div class="brand abs"><span>Boreal</span><span class="brand-mark"></span><span>Voyage</span></div>
  <div class="site-search abs">
    <svg width="11" height="11" viewBox="0 0 11 11"><circle cx="4.5" cy="4.5" r="3.5" fill="none" stroke="#888" stroke-width="1.5"/><line x1="7" y1="7" x2="10" y2="10" stroke="#888" stroke-width="1.5"/></svg>
    SEARCH
  </div>
</header>

<nav class="main-nav abs">
  <span style="left:26px">Home</span>
  <span style="left:113px">Fjords</span>
  <span style="left:212px">Capitals</span>
  <span style="left:328px">Cruises</span>
  <span style="left:438px">Winter</span>
  <span style="left:533px">Pictures</span>
  <span style="left:789px"><i class="flag en"></i>English</span>
  <span style="left:901px"><i class="flag de"></i>German</span>
</nav>

<div class="caption abs">
  <h1>Spectacular Fjords</h1>
  <p>Included on Global Heritage's World Heritage List</p>
</div>
<div class="dots abs"><i></i><i class="on"></i><i></i><i></i></div>

<form class="tour-finder abs">
  <label>Tour Type</label>
  <div class="select">All tour types<svg width="10" height="6" viewBox="0 0 10 6"><path d="M1 1l4 4 4-4" fill="none" stroke="#fff" stroke-width="1.5"/></svg></div>
  <label>Tour Selection</label>
  <div class="select">All tour selections<svg width="10" height="6" viewBox="0 0 10 6"><path d="M1 1l4 4 4-4" fill="none" stroke="#fff" stroke-width="1.5"/></svg></div>
  <label>Travel Period</label>
  <div class="select">All travel periods<svg width="10" height="6" viewBox="0 0 10 6"><path d="M1 1l4 4 4-4" fill="none" stroke="#fff" stroke-width="1.5"/></svg></div>
  <div class="find-btn">Search</div>
</form>

<main>
  <article class="tile abs" style="left:102px;top:708px"><div class="photo" role="img" aria-label="Traveller in a knitted sweater enjoying a snack outdoors" style="background:linear-gradient(135deg,#c9b08a,#6f6a66 60%,#2f2f33)"></div><h2>Scandinavia Specialist</h2><p>Lorem Ipsum is simply dummy<br>text of the printing</p><a>More Details</a></article>
  <article class="tile abs" style="left:352px;top:708px"><div class="photo" role="img" aria-label="Group rafting through white water rapids" style="background:linear-gradient(160deg,#3a3428,#6a6650 50%,#b8b6a8)"></div><h2>Special Offers</h2><p>Lorem Ipsum is simply dummy<br>text of the printing</p><a>More Details</a></article>
  <article class="tile abs" style="left:603px;top:708px"><div class="photo" role="img" aria-label="Person in a dark suit writing on a glass board" style="background:linear-gradient(160deg,#2a2d33,#15171b 60%,#3a3d44)"></div><h2>Contact</h2><p>Lorem Ipsum is simply dummy<br>text of the printing</p><a>More Details</a></article>
  <article class="tile abs" style="left:853px;top:708px"><div class="photo" role="img" aria-label="Traditional wooden station building at dusk" style="background:linear-gradient(180deg,#0f1a33,#3a2a22 55%,#2a221e)"></div><h2>Norway</h2><p>Lorem Ipsum is simply dummy<br>text of the printing</p><a>More Details</a></article>

  <article class="tile abs" style="left:102px;top:1034px"><div class="photo" role="img" aria-label="Red farmhouse on a green hillside" style="background:linear-gradient(180deg,#6f8d3c,#425c23 45%,#5a7a2e)"></div><h2>Sweden</h2><p>Lorem Ipsum is simply dummy<br>text of the printing</p><a>More Details</a></article>
  <article class="tile abs" style="left:352px;top:1034px"><div class="photo" role="img" aria-label="Hikers with a dog crossing a snowy landscape at twilight" style="background:linear-gradient(180deg,#6a5a82,#8a86a8 50%,#b7b8cf)"></div><h2>Iceland</h2><p>Lorem Ipsum is simply dummy<br>text of the printing</p><a>More Details</a></article>
  <article class="tile abs" style="left:603px;top:1034px"><div class="photo" role="img" aria-label="Colourful harbour-side townhouses with café umbrellas" style="background:linear-gradient(180deg,#2c3e66,#8a6a48 45%,#6a3a2a)"></div><h2>Combination Tours</h2><p>Lorem Ipsum is simply dummy<br>text of the printing</p><a>More Details</a></article>
  <article class="tile abs" style="left:853px;top:1034px"><div class="photo" role="img" aria-label="Ornate white palace hall with tall windows" style="background:linear-gradient(180deg,#d8d4c8,#b5ad9c 55%,#6e6254)"></div><h2>Lapland</h2><p>Lorem Ipsum is simply dummy<br>text of the printing</p><a>More Details</a></article>

  <article class="tile abs" style="left:102px;top:1357px"><div class="photo" role="img" aria-label="Blossoming tree above a fjord with snowy mountains" style="background:linear-gradient(180deg,#7a92b0,#9fb0bf 40%,#3f5a4a)"></div><h2>Winter and Northan Lights</h2><p>Lorem Ipsum is simply dummy<br>text of the printing</p><a>More Details</a></article>
  <article class="tile abs" style="left:352px;top:1357px"><div class="photo" role="img" aria-label="Coastal ship moored below steep green mountains" style="background:linear-gradient(180deg,#3d6fa8,#5a7a6a 45%,#1e3040)"></div><h2>Fjords</h2><p>Lorem Ipsum is simply dummy<br>text of the printing</p><a>More Details</a></article>
  <article class="tile abs" style="left:603px;top:1357px"><div class="photo" role="img" aria-label="Cathedral with colourful onion domes against a blue sky" style="background:linear-gradient(180deg,#2c5ea8,#8a5a3a 50%,#7a3a2a)"></div><h2>Capitals</h2><p>Lorem Ipsum is simply dummy<br>text of the printing</p><a>More Details</a></article>

  <aside class="feed abs">
    <div class="feed-head">Socialwall</div>
    <div class="feed-post"><i class="avatar"></i><p><b>Lorem Ipsum</b> is simply dummy text of the printing and typesetting industry</p><span class="meta">9:44pm<em>Comment</em><em>Like</em></span></div>
    <div class="feed-post"><i class="avatar"></i><p><b>Lorem Ipsum</b> is simply dummy text of the printing and typesetting industry</p><span class="meta">9:44pm<em>Comment</em><em>Like</em></span></div>
    <div class="feed-post"><i class="avatar"></i><p><b>Lorem Ipsum</b> is simply dummy text of the printing and typesetting industry</p><span class="meta">9:44pm<em>Comment</em><em>Like</em></span></div>
    <div class="feed-scroll"><i></i></div>
    <div class="feed-foot"><i></i>Socialwall Social Plugin</div>
  </aside>
</main>

<footer class="site-footer abs">
  <div class="footer-col" style="left:106px">
    <h3>Tour Types</h3>
    <ul><li>Escorted Coach Tours</li><li>Independent Rail Tours</li><li>Independent Short Breaks</li><li>Partly Escorted Tours</li><li>Scandinavian Cruises</li><li>Self Drive Tours</li></ul>
    <h3 class="second">Winter Tour Types</h3>
    <ul><li>Norway Winter Tours</li><li>Sweden Winter Tours</li><li>Finland Winter Tours</li><li>Iceland Winter Tours</li></ul>
  </div>
  <i class="footer-rule" style="left:303px"></i>
  <div class="footer-col" style="left:346px">
    <h3>Tour Selections</h3>
    <ul><li>Fjord Tours</li><li>Scandinavian Capitals</li><li>Scandinavia Cruise Packages</li><li>Exclusive Tours</li><li>Midnight Sun</li><li>Activity Tours</li><li>Meet the locals</li><li>Northern lights</li><li>Norway Tours</li><li>Sweden Tours</li><li>Iceland Tours</li><li>Göta Canal Cruises</li><li>Coastal Express Cruises</li></ul>
  </div>
  <i class="footer-rule" style="left:573px"></i>
  <div class="footer-col" style="left:616px">
    <h3>Boreal Voyage</h3>
    <ul><li>About Boreal Voyage</li><li>Booking and Payment Procedure</li><li>Terms and Conditions</li><li>Frequently Asked Questions (FAQ)</li><li>Travel Experiences</li><li>Photo Credits</li><li>Site Map</li><li>Contact</li></ul>
    <h3 class="second">Recently Added Tours</h3>
    <ul><li>Baltic &amp; Russian Explorer</li><li>Iceland Wilderness</li><li>Baltic Classical</li></ul>
  </div>
  <i class="footer-rule" style="left:877px"></i>
  <div class="footer-col" style="left:920px">
    <h3>Winter Selections</h3>
    <ul><li>Norway Winter Cruises</li><li>Ice Hotel Holidays</li><li>Winter Rail Tours</li><li>Lapland Winter Tours</li><li>Winter Weekend Breaks</li><li>Winter Tours Unpolished</li></ul>
  </div>
  <i class="footer-base"></i>
  <div class="connect">Connect With us</div>
  <div class="social"><i></i><i></i><i></i></div>
  <div class="payments"><i></i><i></i><i></i><i></i></div>
  <div class="copyright">Copyrights @ 2015 All Rights Reserved</div>
</footer>

</body>
</html>
```